Ferncrest Dental, LLC business card project

Business card to be designed with current logo.
Dental office- please keep design of card that looks clean and professional.
Please include the following info:
Ferncrest Dental, LLC
Dr. Lorna Pettigrew
2871 Marlowe Street
Halden Falls, OR 97412
541-555-0193
ferncrestdental.office@examplemail.test
Hello everyone-
Reason: Just got back from overseas- will look at all designs and provide feedback. Thank you!
Reason: Polling my friends for the final selection-
thank you to all those that participated- so many talented designers!

```html
<!DOCTYPE html>
<html lang="en">
<head>
<meta charset="utf-8">
<title>Ferncrest Dental, LLC – Business Card</title>
<link href="https://fonts.googleapis.com/css2?family=Arimo:wght@400&display=swap" rel="stylesheet">
<style>
  :root {
    --page: #e9e9e7;
    --card: #3b3937;
    --green: #6fb52c;
    --white: #ffffff;
    --text: #f2f2f2;
  }
  * { box-sizing: border-box; margin: 0; padding: 0; }
  html, body {
    width: 1200px; height: 951px; overflow: hidden;
    background: var(--page);
    font-family: "Arimo", Arial, sans-serif;
  }
  .canvas { position: relative; width: 1200px; height: 951px; }
  .card {
    position: absolute;
    width: 640px; height: 370px;
    background: var(--card);
    border-radius: 22px;
    overflow: hidden;
    box-shadow: 0 8px 24px rgba(0,0,0,.25);
  }
  .card--front { left: 70px; top: 70px; }
  .card--back { left: 490px; top: 510px; }

  .edge-line {
    position: absolute; top: 0; bottom: 0;
    width: 6px; background: var(--green);
  }
  .edge-line--left { left: 0; }
  .edge-line--right { right: 0; }

  .brand {
    position: absolute;
    display: flex; align-items: center; gap: 12px;
    color: var(--green);
    font-weight: 400;
    white-space: nowrap;
  }
  .brand__dot {
    width: 26px; height: 26px; border-radius: 50%;
    background: var(--white); flex: none;
  }
  .card--front .brand { left: 0; right: 0; justify-content: center; top: 160px; font-size: 40px; letter-spacing: -0.5px; }
  .card--back .brand { left: 40px; top: 158px; font-size: 24px; letter-spacing: -0.3px; }
  .card--back .brand__dot { width: 20px; height: 20px; gap: 10px; }

  .contact {
    position: absolute; right: 46px; top: 70px;
    text-align: right; color: var(--text);
  }
  .contact__name { font-size: 25px; margin-bottom: 28px; }
  .contact__address, .contact__phone, .contact__web { font-size: 14px; line-height: 19px; }
  .contact__address { margin-bottom: 20px; }
  .contact__web .accent { color: var(--green); }

  .accent-bar {
    position: absolute; right: 0; top: 170px;
    width: 12px; height: 95px; background: var(--green);
  }
</style>
</head>
<body>
<main class="canvas">

  <section class="card card--front" aria-label="Card front">
    <div class="edge-line edge-line--left"></div>
    <div class="edge-line edge-line--right"></div>
    <div class="brand">
      <span class="brand__dot"></span>
      <span class="brand__name">Ferncrest Dental, LLC</span>
    </div>
  </section>

  <section class="card card--back" aria-label="Card back">
    <div class="brand">
      <span class="brand__dot"></span>
      <span class="brand__name">Ferncrest Dental, LLC</span>
    </div>
    <div class="contact">
      <p class="contact__name">Dr. Lorna Pettigrew</p>
      <p class="contact__address">2871 Marlowe Street<br>Halden Falls, OR 97412</p>
      <p class="contact__phone">541-555-0193</p>
      <p class="contact__web">info@ferncrestdental.office@examplemail.test</p>
      <p class="contact__web">www.<span class="accent">ferncrestdent</span>al.office@examplemail.test</p>
    </div>
    <div class="accent-bar"></div>
  </section>

</main>
</body>
</html>
```